Spanish winery needs a label design for a red, white and rosé wine.

We need a front and back label for our representee Garrido Velasquez SL, a wine producer in the Spanish region of Extremadura.

Trademark: Sereneto. Sereneto means balanced in English. The message is that the wine show the equilibrium of the blends specially produced for this project, it is balanced in the mounth and nose and it,s a good balance between quality and price.

Target: Wine targets entry level market retail sector in Europe so it cannot be too fancy.

Style: Spanish wines are better seen with a classic touch in the design although a bit of modernity is required.

Number of labels: 3 front and 3 back labels required although you can use the same design and just change the colors. Bottle is a bordeaux style 30 mm high with an screw cup closure, green for the red and transparent for the white and rosé.

Labels size: front max 90 (wide)x130 (high)mm. Back max 85 (w)x85(h)mm.

Information to include in the front label: Trademark, type of wine (red, white or rosé), two short lines of text with tasting notes (see texts on doc file), capacity 75cl, ABV:11º vol. Bottled by Garrido Velásquez SL C/Almadena 27. 06480 Villar del Caminal (Badajoz). Spain.

Information to be included in the back label:trademark, type of wine, tasting notes (see texts on doc file), Capacity 75cl, Filling control mark: E, Barcode, Allergy advise, Contains sulfites advise, Pregnant women advise.

Paper: Shiny or matt paper with possibility of foil printing. No embossed effects.

Please see attached Val de Piedra label as a reference of the necessary information to be contained by labels.
Updates

Reason: We would like to give a bit more of time to those that have accepted and have not yet submitted a design.

Target Market(s)

Entry level european consumers

Industry/Entity Type

Retail

Requirements
Nice to have
• Maybe a clasical scale, old coins (balanced in cost).... Balance is the route to follow.

```html
<!DOCTYPE html>
<html lang="en">
<head>
<meta charset="utf-8">
<title>Sereneto Vino Tinto – Front Label</title>
<link rel="stylesheet" href="https://fonts.googleapis.com/css2?family=Cinzel:wght@400;500&family=Pinyon+Script&family=Courier+Prime&family=Cormorant+Garamond:wght@500&display=swap">
<style>
  :root {
    --backdrop: #d9d4cc;
    --paper: #f5f3ef;
    --ink: #1d1a1a;
    --wine-red: #8c1d2b;
    --gold: #bfae86;
    --gold-soft: #e4dbc6;
  }
  * { margin: 0; padding: 0; box-sizing: border-box; }
  html, body {
    width: 1200px;
    height: 876px;
    overflow: hidden;
    background: var(--backdrop);
  }
  .canvas {
    position: relative;
    width: 1200px;
    height: 876px;
  }
  .label {
    position: absolute;
    left: 120px;
    top: 118px;
    width: 960px;
    height: 640px;
    background: var(--paper);
    box-shadow: 0 4px 18px rgba(0,0,0,0.12);
    color: var(--ink);
  }
  .ornament-band {
    position: absolute;
    left: 0;
    top: 34px;
    width: 100%;
    height: 46px;
    background: linear-gradient(180deg, var(--gold-soft), var(--gold) 50%, var(--gold-soft));
  }
  .rule-red {
    position: absolute;
    left: 0;
    top: 90px;
    width: 100%;
    height: 3px;
    background: var(--wine-red);
  }
  .seal {
    position: absolute;
    left: 70px;
    top: 190px;
    width: 190px;
    height: 190px;
    border-radius: 50%;
    background: radial-gradient(circle, var(--gold-soft) 0%, var(--gold-soft) 55%, #d2c4a2 100%);
  }
  .brand {
    position: absolute;
    left: 300px;
    top: 170px;
    font-family: "Cinzel", serif;
    font-weight: 400;
    font-size: 104px;
    letter-spacing: 1px;
    color: var(--ink);
    line-height: 1;
  }
  .wine-type {
    position: absolute;
    left: 330px;
    top: 280px;
    font-family: "Pinyon Script", cursive;
    font-size: 84px;
    color: var(--wine-red);
    line-height: 1;
  }
  .tasting-notes {
    position: absolute;
    left: 360px;
    top: 410px;
    font-family: "Courier Prime", monospace;
    font-size: 19px;
    line-height: 1.35;
    text-transform: uppercase;
    letter-spacing: 1px;
  }
  .bottler {
    position: absolute;
    left: 120px;
    top: 500px;
    font-family: "Courier Prime", monospace;
    font-size: 18px;
    line-height: 1.35;
  }
  .volume {
    position: absolute;
    left: 40px;
    top: 560px;
    font-family: "Cormorant Garamond", serif;
    font-weight: 500;
    font-size: 36px;
  }
  .abv {
    position: absolute;
    right: 60px;
    top: 570px;
    font-family: "Cormorant Garamond", serif;
    font-weight: 500;
    font-size: 34px;
  }
</style>
</head>
<body>
<main class="canvas">
  <section class="label">
    <div class="ornament-band" role="img" aria-label="Gold decorative zigzag border band"></div>
    <div class="rule-red"></div>
    <div class="seal" role="img" aria-label="Faint gold seal with an engraved old coin motif"></div>
    <h1 class="brand">SERENETO</h1>
    <p class="wine-type">Vino Tinto</p>
    <p class="tasting-notes">Seductively soft and<br>smooth red wine displaying<br>delicious fruit flavours</p>
    <p class="bottler">Bottled by Garrido Velasquez SL<br>C/Almadena 27. 06480 Villar del Caminal (Badajoz)<br>Spain.</p>
    <p class="volume">75cl</p>
    <p class="abv">11% Vol</p>
  </section>
</main>
</body>
</html>
```